Tender Scout Letterhead Design Project

We need a letterhead design for a consultancy business based in Australia.

Tender Scout is a unique business designed to assist with the complex and time consuming nature of selecting contractors, showing them what to do and reviewing quotes when it comes to body corporate and strata maintenance items such as painting, waterproofing, plumbing and electrical.

Target Market(s)

apartment managers

Industry/Entity Type

Business

Requirements
Must have
• must have logo and contact details

Tender Scout
82 Wallaroo Creek Road
Yandara, QLD 4571
Ph 07 5391 2846
Fax 07 5327 6018
Mobile 0438 917304

```html
<!DOCTYPE html>
<html lang="en">
<head>
<meta charset="utf-8">
<title>Tender Scout Letterhead</title>
<link rel="stylesheet" href="https://fonts.googleapis.com/css2?family=Fira+Sans:wght@400;600;800&family=Courier+Prime&display=swap">
<style>
  :root {
    --ink: #111111;
    --frame: #000000;
    --paper: #ffffff;
    --orange: #f7931e;
    --red: #ed1c24;
    --green: #a6d92a;
    --mark-grey: #cdd2d2;
    --orange-tint: #fdebd8;
    --red-tint: #fcdcdc;
  }
  * { box-sizing: border-box; margin: 0; padding: 0; }
  html, body { width: 927px; height: 1200px; overflow: hidden; background: var(--paper); }
  .letterhead {
    position: relative;
    width: 927px;
    height: 1200px;
    background: var(--paper);
    border: 4px solid var(--frame);
    font-family: "Fira Sans", sans-serif;
    color: var(--ink);
    overflow: hidden;
  }
  .watermark {
    position: absolute;
    top: 0;
    left: 0;
    width: 919px;
    height: 1192px;
  }
  .company-heading {
    position: absolute;
    left: 44px;
    top: 40px;
    font-weight: 800;
    font-size: 22px;
    letter-spacing: 4.7px;
    line-height: 1;
  }
  .address {
    position: absolute;
    left: 70px;
    top: 80px;
    font-size: 16.5px;
    line-height: 23px;
    font-style: normal;
  }
  .contacts {
    position: absolute;
    left: 70px;
    top: 131px;
    list-style: none;
    font-size: 16.5px;
    line-height: 24px;
  }
  .contacts .label {
    font-family: "Courier Prime", monospace;
    font-size: 18px;
    margin-right: 4px;
  }
  .label-phone { color: var(--orange); }
  .label-fax { color: var(--red); }
  .label-mobile { color: var(--green); }
  .contacts .label-mobile { margin-right: 10px; }
  .brand {
    position: absolute;
    left: 52px;
    top: 1072px;
    display: flex;
    align-items: center;
    gap: 14px;
  }
  .brand-name {
    font-weight: 600;
    font-size: 90px;
    line-height: 1;
    letter-spacing: -1px;
    color: var(--mark-grey);
  }
  .brand-dot {
    width: 34px;
    height: 34px;
    border-radius: 50%;
    background: var(--orange);
    margin-top: 20px;
  }
</style>
</head>
<body>
  <main class="letterhead">
    <svg class="watermark" viewBox="0 0 919 1192" aria-hidden="true">
      <circle cx="886" cy="212" r="80" fill="var(--orange-tint)"/>
      <circle cx="760" cy="496" r="98" fill="var(--red-tint)"/>
    </svg>
    <h1 class="company-heading">TENDER SCOUT</h1>
    <address class="address">
      82 Wallaroo Creek Road<br>
      Yandara, QLD 4571
    </address>
    <ul class="contacts">
      <li><span class="label label-phone">PH</span>07 5391 2846</li>
      <li><span class="label label-fax">FAX</span>07 5327 6018</li>
      <li><span class="label label-mobile">MOBILE</span>0438 917304</li>
    </ul>
    <div class="brand">
      <span class="brand-name">Tender Scout</span>
      <span class="brand-dot" aria-hidden="true"></span>
    </div>
  </main>
</body>
</html>
```